Harrowmere Fields Green Initiative Infographic

We need a flyer to distribute to new and existing tenants in our office park which explains our Green Initiatives. Harrowmere Fields Office Park is a Class A office park consisting of 5 commercial buildings and about 100 tenants. Some of our clients include Quillbyte, Vantorell and Dunmore Bask.

Please visit www.harrowmerefieldsofficepark.example for questions on our current "brand" and amenities. It is very important to follow the current “feel” we have on the website.

Here are the Green Initiatives we need to convey in this flyer:
1. All buildings Power Crest rated in 2009
2. Lighting and Energy Initiatives:
a.) Motion sensors added to all electrical and janitorial closest, storage areas and executive parking garages b.) Relamp from a 32W to a 28W bulb for all 2x4 fixtures in tenant offices and building common areas c.) Stairways relamped to 25W
d.) Relamped from T12 to T8 and LEDS in elevator cabs
e.) Relamped to LEDs in Elevators Lobby
f.) Relamped Restrooms to Compact Fluorescent

3. Plumbing: installed aerators on restroom faucets at .5 gallon per minute

4. Heating Ventilation Air Conditioning (HVAC) Energy Management System programming engineered for best performance. Secondly, all rooftop units have VFDs (Variable Frequency Drives) which controls fan speed for optimal efficiency.

5. Irrigation Systems all have rain sensors

6. Comprehensive recycling program includes the recycling of plastic, glass, cans, all types of paper, and cardboard. Secondly, construction recycling is required and captures about 70% for recycling

7. Implemented green contracts with janitorial, window cleaning, and pest control.

8. Sustainable purchasing procedures include items such as green cleaning products for janitorial and window cleaning

9. Annual Building Events such as a Page Trade where tenants donate used books in exchange for another book and the Transit Expo which partners with community partners: 781 Rideshare Services and the RVB Urban Rail Network.

10. 2013 earth day celebration will include a green fair, recycling awareness, education, commuting options, and several educational awareness events

Reason: Please submit designs as inforgraphics. Thank you.

• Must have:
"Harrowmere Fields Office Park" as prominent, same feel as website listed above, include all 10 initiaves,

```html
<!DOCTYPE html>
<html lang="en">
<head>
<meta charset="utf-8">
<title>The Green Initiatives of Harrowmere Fields Office Park</title>
<link href="https://fonts.googleapis.com/css2?family=Arimo:wght@400;700&display=swap" rel="stylesheet">
<style>
:root{
  --page:#ffffff;
  --card:#e4e8d4;
  --band:#c8d1a8;
  --ink:#3a3d3a;
  --rule:#6b6f68;
  --sage:#a7b690;
  --sage-dark:#7d8f6c;
  --slate:#5a6566;
  --brass:#a89458;
}
*{box-sizing:border-box;margin:0;padding:0}
html,body{width:960px;height:1200px;overflow:hidden;background:var(--page)}
body{font-family:"Arimo",Arial,sans-serif;color:var(--ink)}
.canvas{position:relative;width:960px;height:1200px}
.flyer{position:absolute;left:73px;top:73px;width:814px;height:1054px;background:var(--card)}
.title-band{position:absolute;left:111px;top:113px;width:738px;height:43px;background:var(--band);border:1px solid var(--rule);
  display:flex;align-items:center;justify-content:center;font-size:25px;font-weight:700;color:#3b3e3b;letter-spacing:-.2px}
.divider{position:absolute;left:480px;top:187px;width:1px;height:840px;background:var(--rule)}
.rule{position:absolute;height:1px;background:var(--rule)}
.rule.left{left:111px;width:350px}
.rule.right{left:500px;width:349px}
.badge{position:absolute;width:19px;height:19px;background:var(--band);font-size:13px;font-weight:700;
  display:flex;align-items:center;justify-content:center;color:#3b3e3b}
.item-text{position:absolute;font-size:12.5px;line-height:17px;color:var(--ink)}
.icon{position:absolute}
.footer-name{position:absolute;left:153px;top:1054px;display:flex;align-items:center;gap:12px;font-size:20px;color:#3f4340;letter-spacing:1.5px}
.footer-name .mark{width:26px;height:26px;border-radius:50%;background:var(--sage-dark)}
.managed-by{position:absolute;left:520px;top:1042px;font-size:9px;color:var(--ink)}
.managers{position:absolute;left:520px;top:1062px;display:flex;align-items:center;gap:14px;font-size:17px;font-weight:700;color:#4a4d4a}
.managers .sep{width:1px;height:30px;background:var(--rule)}
</style>
</head>
<body>
<div class="canvas">
  <div class="flyer"></div>
  <h1 class="title-band">The Green Initiatives of Harrowmere Fields Office Park</h1>
  <div class="divider"></div>

  <!-- Left column -->
  <div class="badge" style="left:111px;top:196px">1</div>
  <p class="item-text" style="left:144px;top:196px;width:200px">All buildings Power Crest rated in 2009.</p>
  <div class="icon" style="left:380px;top:193px;width:60px;height:58px;background:var(--slate)" role="img" aria-label="Rating certificate badge"></div>
  <div class="rule left" style="top:271px"></div>

  <div class="badge" style="left:111px;top:296px">2</div>
  <p class="item-text" style="left:144px;top:297px">Lighting and Energy Initiatives:</p>
  <div class="rule left" style="top:333px"></div>

  <div class="badge" style="left:111px;top:353px">A</div>
  <p class="item-text" style="left:144px;top:355px;width:215px">Motion sensors added to all electrical and janitorial closest, storage areas and executive parking garages.</p>
  <svg class="icon" style="left:380px;top:353px" width="28" height="60" viewBox="0 0 28 60"><rect x="1" y="1" width="26" height="58" rx="3" fill="var(--sage)" stroke="var(--slate)"/><rect x="6" y="8" width="16" height="20" fill="#eef0e4" stroke="var(--slate)"/><rect x="9" y="44" width="10" height="4" fill="var(--slate)"/></svg>
  <div class="rule left" style="top:433px"></div>

  <div class="badge" style="left:111px;top:453px">B</div>
  <p class="item-text" style="left:144px;top:454px;width:200px">Relamp from a 32w to a 28w bulb for all 2x4 fixtures in tenant offices and building common areas.</p>
  <svg class="icon" style="left:356px;top:455px" width="108" height="70" viewBox="0 0 108 70">
    <circle cx="22" cy="22" r="20" fill="var(--sage)"/><rect x="14" y="40" width="16" height="14" fill="var(--brass)"/><text x="22" y="27" font-size="13" text-anchor="middle" font-family="Arimo,sans-serif" fill="#333">32w</text>
    <path d="M46 24h10v-7l10 11-10 11v-7H46z" fill="var(--slate)"/>
    <circle cx="86" cy="22" r="20" fill="var(--sage)"/><rect x="78" y="40" width="16" height="14" fill="var(--brass)"/><text x="86" y="27" font-size="13" text-anchor="middle" font-family="Arimo,sans-serif" fill="#333">28w</text>
  </svg>
  <div class="rule left" style="top:533px"></div>

  <div class="badge" style="left:111px;top:556px">C</div>
  <p class="item-text" style="left:144px;top:557px">Stairways relamped to 25w.</p>
  <svg class="icon" style="left:390px;top:556px" width="42" height="66" viewBox="0 0 42 66"><circle cx="21" cy="21" r="20" fill="var(--sage)"/><rect x="13" y="39" width="16" height="16" fill="var(--brass)"/><text x="21" y="26" font-size="13" text-anchor="middle" font-family="Arimo,sans-serif" fill="#333">25w</text></svg>
  <div class="rule left" style="top:633px"></div>

  <div class="badge" style="left:111px;top:653px">D</div>
  <p class="item-text" style="left:144px;top:654px;width:180px">Relamped from T12 to T8 and LEDS in elevator cabs.</p>
  <svg class="icon" style="left:356px;top:653px" width="108" height="68" viewBox="0 0 108 68">
    <rect x="6" y="10" width="30" height="52" rx="3" fill="var(--sage)"/><rect x="12" y="2" width="3" height="8" fill="var(--brass)"/><rect x="27" y="2" width="3" height="8" fill="var(--brass)"/><text x="21" y="42" font-size="13" text-anchor="middle" font-family="Arimo,sans-serif" fill="#333">T12</text>
    <path d="M44 34h10v-7l10 11-10 11v-7H44z" fill="var(--slate)"/>
    <rect x="72" y="10" width="30" height="52" rx="3" fill="var(--sage)"/><rect x="78" y="2" width="3" height="8" fill="var(--brass)"/><rect x="93" y="2" width="3" height="8" fill="var(--brass)"/><text x="87" y="42" font-size="13" text-anchor="middle" font-family="Arimo,sans-serif" fill="#333">T8</text>
  </svg>
  <div class="rule left" style="top:737px"></div>

  <div class="badge" style="left:111px;top:753px">E</div>
  <p class="item-text" style="left:144px;top:754px;width:180px">Relamped to LEDs in Elevators Lobby.</p>
  <svg class="icon" style="left:387px;top:757px" width="54" height="54" viewBox="0 0 54 54"><circle cx="27" cy="27" r="26" fill="var(--slate)"/><g fill="#d6dcc4"><circle cx="27" cy="14" r="5"/><circle cx="38" cy="21" r="5"/><circle cx="38" cy="34" r="5"/><circle cx="27" cy="40" r="5"/><circle cx="16" cy="34" r="5"/><circle cx="16" cy="21" r="5"/><circle cx="27" cy="27" r="5"/></g></svg>
  <div class="rule left" style="top:827px"></div>

  <div class="badge" style="left:111px;top:849px">F</div>
  <p class="item-text" style="left:144px;top:850px;width:170px">Relamped Restrooms to Compact Fluorescent.</p>
  <svg class="icon" style="left:356px;top:847px" width="108" height="66" viewBox="0 0 108 66">
    <g fill="var(--sage)"><rect x="8" y="2" width="6" height="42" rx="3"/><rect x="17" y="2" width="6" height="42" rx="3"/><rect x="26" y="2" width="6" height="42" rx="3"/><rect x="35" y="2" width="6" height="42" rx="3"/>
    <rect x="66" y="2" width="6" height="42" rx="3"/><rect x="75" y="2" width="6" height="42" rx="3"/><rect x="84" y="2" width="6" height="42" rx="3"/><rect x="93" y="2" width="6" height="42" rx="3"/></g>
    <rect x="6" y="44" width="37" height="8" fill="var(--slate)"/><rect x="15" y="52" width="19" height="10" fill="var(--brass)"/>
    <rect x="64" y="44" width="37" height="8" fill="var(--slate)"/><rect x="73" y="52" width="19" height="10" fill="var(--brass)"/>
  </svg>
  <div class="rule left" style="top:927px"></div>

  <div class="badge" style="left:111px;top:947px">3</div>
  <p class="item-text" style="left:144px;top:948px;width:190px">Plumbing: installed aerators on restroom faucets at .5 gallon per minute.</p>
  <svg class="icon" style="left:358px;top:938px" width="50" height="70" viewBox="0 0 50 70"><rect x="20" y="0" width="10" height="8" fill="var(--brass)"/><path d="M25 8 L48 66 H2 Z" fill="#eef0e4" stroke="var(--slate)"/><text x="25" y="52" font-size="16" text-anchor="middle" font-family="Arimo,sans-serif" fill="#333">.5</text><text x="25" y="63" font-size="8" text-anchor="middle" font-family="Arimo,sans-serif" fill="#333">Gallon</text></svg>
  <div class="rule left" style="top:1027px"></div>

  <!-- Right column -->
  <div class="badge" style="left:500px;top:196px">4</div>
  <p class="item-text" style="left:540px;top:197px;width:225px">Heating Ventilation Air Conditioning (HVAC) Energy Management System programming engineered for best performance. Secondly, all rooftop units have VFDs (Variable Frequency Drives) which controls fan speed for optimal efficiency.</p>
  <svg class="icon" style="left:770px;top:196px" width="76" height="68" viewBox="0 0 76 68"><g fill="var(--sage)" stroke="var(--slate)"><ellipse cx="38" cy="16" rx="11" ry="16"/><ellipse cx="38" cy="52" rx="11" ry="16"/><ellipse cx="20" cy="34" rx="17" ry="10"/><ellipse cx="56" cy="34" rx="17" ry="10"/></g><circle cx="38" cy="34" r="6" fill="#eef0e4" stroke="var(--slate)"/></svg>
  <div class="rule right" style="top:327px"></div>

  <div class="badge" style="left:500px;top:345px">5</div>
  <p class="item-text" style="left:540px;top:346px;width:190px">Irrigation Systems all have rain sensors.</p>
  <svg class="icon" style="left:752px;top:344px" width="98" height="58" viewBox="0 0 98 58"><g fill="var(--sage)" stroke="var(--slate)"><path id="drop" d="M10 2 C14 10 18 14 18 19 a8 8 0 0 1-16 0 C2 14 6 10 10 2Z"/><use href="#drop" x="24"/><use href="#drop" x="48"/><use href="#drop" x="72"/><use href="#drop" y="30"/><use href="#drop" x="24" y="30"/><use href="#drop" x="48" y="30"/><use href="#drop" x="72" y="30"/></g></svg>
  <div class="rule right" style="top:420px"></div>

  <div class="badge" style="left:500px;top:444px">6</div>
  <p class="item-text" style="left:540px;top:445px;width:205px">Comprehensive recycling program includes the recycling of plastic, glass, cans, all types of paper, and cardboard. Secondly, construction recycling is required and captures about 70% for recycling.</p>
  <div class="icon" style="left:780px;top:440px;width:66px;height:66px;border-radius:50%;background:var(--sage)" role="img" aria-label="Recycling symbol"></div>
  <div class="rule right" style="top:557px"></div>

  <div class="badge" style="left:500px;top:580px">7</div>
  <p class="item-text" style="left:540px;top:582px;width:205px">Implemented green contracts with janitorial, window cleaning, and pest control.</p>
  <div class="icon" style="left:784px;top:576px;width:57px;height:57px;border-radius:50%;background:var(--sage)" role="img" aria-label="Pest control emblem with crossed-out insect"></div>
  <div class="rule right" style="top:657px"></div>

  <div class="badge" style="left:500px;top:682px">8</div>
  <p class="item-text" style="left:540px;top:683px;width:210px">Sustainable purchasing procedures include items such as green cleaning products for janitorial and window cleaning.</p>
  <svg class="icon" style="left:786px;top:680px" width="62" height="48" viewBox="0 0 62 48"><rect x="0" y="0" width="62" height="8" fill="var(--slate)"/><rect x="27" y="8" width="8" height="40" fill="var(--slate)"/></svg>
  <div class="rule right" style="top:760px"></div>

  <div class="badge" style="left:500px;top:782px">9</div>
  <p class="item-text" style="left:540px;top:784px;width:215px">Annual Building Events such as a Page Trade where tenants donate used books in exchange for another book and the Transit Expo which partners with community partners: 781 Rideshare Services and the RVB Urban Rail Network.</p>
  <div class="icon" style="left:773px;top:780px;width:74px;height:106px;background:linear-gradient(160deg,var(--sage),var(--sage-dark))" role="img" aria-label="Two books exchanged with circular arrows"></div>
  <div class="rule right" style="top:911px"></div>

  <div class="badge" style="left:500px;top:932px">10</div>
  <p class="item-text" style="left:540px;top:933px;width:215px">2013 earth day celebration will include a green fair, recycling awareness, education, commuting options, and several educational awareness events.</p>
  <div class="icon" style="left:780px;top:932px;width:67px;height:67px;border-radius:50%;background:radial-gradient(circle at 35% 35%,#9fb0ae,var(--slate))" role="img" aria-label="Globe of the Earth"></div>
  <div class="rule right" style="top:1027px"></div>

  <!-- Footer -->
  <div class="footer-name"><span class="mark"></span><span>HARROWMERE FIELDS</span></div>
  <p class="managed-by">Property managed by</p>
  <div class="managers"><span>HALVORSEN &amp; PIKE</span><span class="sep"></span><span>BRIGHTMARSH</span></div>
</div>
</body>
</html>
```